Web design project for exciting Australian start-up

Background
We are looking for a creative and talented web design artist to work alongside our market leading web developer.
• You will be required to create a modern and clean design theme for our website, incorporating selected rustic colour scheme elements for our exciting Australian start-up to operate within the coffee industry.
reoccurring work to be expected to flow to the successful designer.
Requirements
• c. 5 - 10 page website
• Landing page
• Log in/ out
• 404 template
• Typography is emphasised
• Please use either a) quillnest.com, b) free web fonts, c) plovra fonts
• All design elements in vector format
• Preferably with icons for each header title(i.e. about us, how it works etc) but designer have free reign over how the site looks, so might not be applicable
• All pages to be responsive
• Down to Kelvo resolution

High level visual design brief attached - additional pages to be worked from base design.

Design inspiration
• We would like to use design elements from the following sources:
http://www.plovra.com/vintel/ (Functionality)
Colour scheme refer to logo and complementary style guide

```html
<!DOCTYPE html>
<html lang="en">
<head>
<meta charset="utf-8">
<title>Brewhaven – Australia First Online Coffee Marketplace</title>
<link rel="stylesheet" href="https://fonts.googleapis.com/css2?family=Open+Sans:wght@300;400;700&family=Roboto+Slab:wght@300;400&family=Libre+Baskerville&display=swap">
<style>
:root{
  --white:#ffffff;
  --ink:#333333;
  --muted:#555555;
  --orange:#ff9f36;
  --red:#e9383f;
  --nav-active:#f3f3f3;
  --nav-line:#ececec;
  --footer-bg:#e8e8e8;
  --footer-dark:#4b4b4b;
  --footer-rule:#6a6a6a;
  --hero-dark:#3a1a0c;
  --hero-mid:#8a3e1c;
  --hero-warm:#c96a3a;
}
*{margin:0;padding:0;box-sizing:border-box}
html,body{width:1200px;height:950px;overflow:hidden;background:var(--white)}
body{position:relative;font-family:"Roboto Slab",serif;color:var(--ink)}

.site-header{position:absolute;left:0;top:0;width:1200px;height:107px;background:var(--white)}
.brand{position:absolute;left:161px;top:36px;display:flex;align-items:center;gap:10px}
.brand-mark{width:34px;height:34px;border-radius:50%;background:var(--orange)}
.brand-name{font-family:"Open Sans",sans-serif;font-weight:700;font-size:26px;letter-spacing:2px;color:#222;text-transform:uppercase}

.main-nav{position:absolute;left:560px;top:0;height:107px;display:flex}
.nav-item{height:107px;display:flex;flex-direction:column;align-items:center;justify-content:center;gap:6px;
  font-family:"Open Sans",sans-serif;font-size:12px;color:#444;text-transform:uppercase;border-right:1px solid var(--nav-line)}
.nav-item:first-child{border-left:1px solid var(--nav-line)}
.nav-item.is-active{background:var(--nav-active)}
.nav-about{width:94px}.nav-how{width:135px}.nav-faq{width:66px}
.nav-item svg{width:20px;height:20px}

.auth-btn{position:absolute;top:38px;height:31px;width:76px;border-radius:2px;color:var(--white);
  font-family:"Roboto Slab",serif;font-size:14px;display:flex;align-items:center;justify-content:center}
.btn-login{left:878px;background:var(--orange)}
.btn-signup{left:963px;background:var(--red)}

.hero{position:absolute;left:0;top:107px;width:1200px;height:543px;
  background:radial-gradient(ellipse 40% 45% at 55% 40%,var(--hero-warm),transparent 70%),
  linear-gradient(180deg,var(--hero-mid) 0%,#6e2f14 55%,var(--hero-dark) 100%)}
.hero-text{position:absolute;left:0;width:1200px;text-align:center;color:var(--white);font-family:"Open Sans",sans-serif}
.hero-kicker{top:210px;font-weight:300;font-size:22px}
.hero-title{top:240px;font-weight:700;font-size:37px;letter-spacing:0.5px}
.hero-cta{position:absolute;left:519px;top:302px;width:162px;height:45px;background:var(--orange);border-radius:2px;
  color:var(--white);font-family:"Roboto Slab",serif;font-size:17px;display:flex;align-items:center;justify-content:center}
.hero-arrow{position:absolute;top:239px;width:57px;height:57px;border:2px solid var(--white);border-radius:50%;
  display:flex;align-items:center;justify-content:center}
.arrow-prev{left:161px}.arrow-next{left:981px}

.site-footer{position:absolute;left:0;top:650px;width:1200px;height:236px;background:var(--footer-bg)}
.footer-col{position:absolute;top:50px}
.col-info{left:295px}.col-who{left:541px}.col-join{left:797px}
.footer-heading{font-family:"Libre Baskerville",serif;font-weight:400;font-size:18px;color:#222;text-transform:uppercase;margin-bottom:14px}
.footer-links{list-style:none}
.footer-links li{height:31px;font-size:14px;font-weight:300;color:var(--muted);display:flex;align-items:center}
.col-who .footer-links li,.col-join .footer-links li{padding-left:3px}
.social-name{width:76px}
.social-dot{width:11px;height:11px;background:#555;border-radius:2px}

.footer-bottom{position:absolute;left:0;top:886px;width:1200px;height:64px;background:var(--footer-dark)}
.footer-rule{position:absolute;left:161px;top:5px;width:878px;height:1px;background:var(--footer-rule)}
.copyright{position:absolute;left:0;top:22px;width:1200px;text-align:center;color:var(--white);font-size:14px;font-weight:300}
</style>
</head>
<body>
<header class="site-header">
  <div class="brand"><span class="brand-mark"></span><span class="brand-name">Brewhaven</span></div>
  <nav class="main-nav">
    <div class="nav-item nav-about is-active">
      <svg viewBox="0 0 20 20" fill="none" stroke="#ff9f36" stroke-width="1.3"><path d="M3 10 L10 3 L17 10"/><path d="M5 8.5 V17 H15 V8.5"/><path d="M8.5 17 V12 H11.5 V17"/></svg>
      About us
    </div>
    <div class="nav-item nav-how">
      <svg viewBox="0 0 20 20" fill="none" stroke="#666" stroke-width="1.2"><circle cx="8" cy="8" r="3"/><path d="M2 18 C2 13 14 13 14 18"/><rect x="12" y="2" width="6" height="5"/></svg>
      How it works
    </div>
    <div class="nav-item nav-faq">
      <svg viewBox="0 0 20 20" fill="none" stroke="#666" stroke-width="1.2"><rect x="4" y="5" width="3" height="13"/><rect x="9" y="3" width="3" height="15"/><path d="M14 2 V18"/></svg>
      FAQ
    </div>
  </nav>
  <a class="auth-btn btn-login">Login</a>
  <a class="auth-btn btn-signup">Sign up</a>
</header>

<section class="hero" role="img" aria-label="Photo of a coffee cup on a saucer beside an old wooden grinder drawer, surrounded by roasted coffee beans">
  <div class="hero-arrow arrow-prev"><svg width="14" height="20" viewBox="0 0 14 20" fill="none" stroke="#fff" stroke-width="2"><path d="M10 3 L4 10 L10 17"/></svg></div>
  <p class="hero-text hero-kicker">AUSTRALIA FIRST ONLINE</p>
  <h1 class="hero-text hero-title">COFFEE MARKETPLACE</h1>
  <a class="hero-cta">Watch Video</a>
  <div class="hero-arrow arrow-next"><svg width="14" height="20" viewBox="0 0 14 20" fill="none" stroke="#fff" stroke-width="2"><path d="M4 3 L10 10 L4 17"/></svg></div>
</section>

<footer class="site-footer">
  <div class="footer-col col-info">
    <h2 class="footer-heading">Helpful Info</h2>
    <ul class="footer-links"><li>About Us</li><li>Media Enquiries</li><li>Terms &amp; Conditions</li><li>Privacy Policy</li></ul>
  </div>
  <div class="footer-col col-who">
    <h2 class="footer-heading">Who We Are</h2>
    <ul class="footer-links"><li>How it works</li><li>FAQ</li><li>Contact us</li></ul>
  </div>
  <div class="footer-col col-join">
    <h2 class="footer-heading">Join Us On</h2>
    <ul class="footer-links">
      <li><span class="social-name">Friendloop</span><span class="social-dot"></span></li>
      <li><span class="social-name">Chirpline</span><span class="social-dot"></span></li>
      <li><span class="social-name">Workweave</span><span class="social-dot"></span></li>
      <li><span class="social-name">Reelcast</span><span class="social-dot"></span></li>
    </ul>
  </div>
</footer>
<div class="footer-bottom">
  <div class="footer-rule"></div>
  <p class="copyright">Copyright © 2014 Brewhaven</p>
</div>
</body>
</html>
```